Business Card Design

A logo and business card design is required for a new podiatry business based on the Great Ocean Road, Victoria, Australia. The business will provide broad array of podiatry services to communities along the coast.

A distinctive design is sought that represents both professional allied health service delivery and the iconic location of the service, where the ocean meets the Otway ranges. Colours representative of the ocean blues, greens of the local forrest would be desirable.

Target Market(s)

GP's, other allied health professionals, members of the community with foot complaints

Industry/Entity Type

Health

Contact Information for Business Card

Tidewater Bend Podiatry
Gareth Linwell
B.Pod B App Sci (HM)
Phone: 0400 718 306
Email: tidewaterbendpodiatry@mailbrook.net

Requirements
Must have
• On the back of the card room allocated for appointment times.
Nice to have
• Would like the logo to incorporate a foot and the elements of the coast, whether it be ocean &/or the unique elements of the coast and the great ocean road.

```html
<!DOCTYPE html>
<html lang="en">
<head>
<meta charset="utf-8">
<title>Tidewater Bend Podiatry – Business Card</title>
<link rel="stylesheet" href="https://fonts.googleapis.com/css2?family=Play:wght@400;700&display=swap">
<style>
  :root {
    --backdrop: #e9e6e1;
    --card: #fbfbfb;
    --teal: #1a9e9a;
    --ink: #2a2a2a;
    --shadow: rgba(0, 0, 0, 0.28);
  }
  html, body {
    margin: 0;
    width: 1200px;
    height: 1000px;
    overflow: hidden;
    background: var(--backdrop);
    font-family: "Play", sans-serif;
  }
  .stage {
    position: relative;
    width: 1200px;
    height: 1000px;
  }
  .business-card {
    position: absolute;
    left: 150px;
    top: 242px;
    width: 900px;
    height: 515px;
    background: var(--card);
    box-shadow: 0 12px 30px var(--shadow);
    border-radius: 4px;
    box-sizing: border-box;
  }
  .brand {
    position: absolute;
    left: 110px;
    top: 78px;
    display: flex;
    align-items: center;
    gap: 28px;
  }
  .brand-name {
    margin: 0;
    font-weight: 700;
    font-size: 44px;
    line-height: 1.1;
    color: var(--teal);
    letter-spacing: 1px;
  }
  .brand-mark {
    width: 96px;
    height: 96px;
    flex: none;
  }
  .person {
    position: absolute;
    left: 0;
    right: 0;
    top: 200px;
    text-align: center;
  }
  .person-name {
    margin: 0;
    font-weight: 700;
    font-size: 42px;
    color: var(--teal);
    letter-spacing: 1px;
  }
  .person-credentials {
    margin: 6px 0 0;
    font-size: 20px;
    color: var(--ink);
    letter-spacing: 1px;
  }
  .contact {
    position: absolute;
    left: 180px;
    top: 330px;
    margin: 0;
    font-size: 30px;
    color: var(--ink);
  }
  .contact-row {
    margin: 0 0 26px;
    display: flex;
    gap: 6px;
  }
  .contact-label {
    color: var(--teal);
  }
</style>
</head>
<body>
<main class="stage">
  <section class="business-card" aria-label="Business card front">
    <header class="brand">
      <h1 class="brand-name">Tidewater Bend Podiatry</h1>
      <svg class="brand-mark" viewBox="0 0 96 96" aria-hidden="true">
        <circle cx="48" cy="48" r="44" fill="var(--teal)"/>
      </svg>
    </header>

    <div class="person">
      <h2 class="person-name">Gareth Linwell</h2>
      <p class="person-credentials">B.Pod B App Sci (HM)</p>
    </div>

    <dl class="contact">
      <div class="contact-row">
        <dt class="contact-label">Phone:</dt>
        <dd style="margin:0">0400 718 306</dd>
      </div>
      <div class="contact-row">
        <dt class="contact-label">Email:</dt>
        <dd style="margin:0">tidewaterbendpodiatry@mailbrook.net</dd>
      </div>
    </dl>
  </section>
</main>
</body>
</html>
```